Quorvex clinic business card - double sided for young clinic

I require business cards for my aesthetic clinic specialising in the below treatments. I would like the cards to be modern as my clinic base are young 22-35 years old. I require my logo on it and would like the edges to be rounded.

I have an aesthetic clinic specialising in :
Quorvex
Lip Enhancement
Chemical Peels
Facial Fillers
Non Surgical Face Lift

I would the cards to have the following information on them:
My logo - (in grey/silver)
address
Phone number
services

Colours :
White/grey/silver and red

a nice image on there, perhaps a set of lips as this is a main service i deliver

Company Name: PDA Address: 52 Farrowmere Road, 4 Brackwell High Street, KT9 4WQ Phone: 0208 794 2160 Website: www.penningtondoweaesthetics.co.uk

Target Market(s)

clinics 22-45 years old mainly female

Industry/Entity Type

Business

Contact Information for Business Card

as above

Requirements
Must have
• logo
• Address
• Email
• Phone number
• Services i offer
Nice to have
• images

```html
<!DOCTYPE html>
<html lang="en">
<head>
<meta charset="utf-8">
<title>Pennington Dowe Aesthetics – Business Card</title>
<link rel="stylesheet" href="https://fonts.googleapis.com/css2?family=Open+Sans:wght@400;600;700&display=swap">
<style>
  :root {
    --stage: #e9e9e9;
    --card-white: #ffffff;
    --ink: #2b2b2b;
    --ink-soft: #3a3a3a;
    --logo-grey: #9a9a9a;
    --rule: #c8c8c8;
    --accent-red: #e0141e;
    --accent-black: #1c1c1c;
    --silver-light: #d2d2d2;
    --silver-mid: #a9a9a9;
    --silver-dark: #8c8c8c;
    --on-silver: #ffffff;
  }
  * { margin: 0; padding: 0; box-sizing: border-box; }
  html, body { width: 1200px; height: 913px; overflow: hidden; }
  body {
    background: var(--stage);
    font-family: "Open Sans", Arial, sans-serif;
    position: relative;
  }
  .card {
    position: absolute;
    top: 311px;
    width: 500px;
    height: 290px;
    border-radius: 22px;
    box-shadow: 0 6px 18px rgba(0,0,0,0.18);
    overflow: hidden;
  }
  /* front */
  .card-front { left: 60px; background: var(--card-white); }
  .brand {
    position: absolute;
    display: flex;
    align-items: center;
    gap: 12px;
  }
  .brand-dot {
    width: 46px; height: 46px; border-radius: 50%;
    background: var(--logo-grey);
    flex: none;
  }
  .brand-name {
    font-weight: 600;
    font-size: 15px;
    line-height: 1.25;
    letter-spacing: 2.5px;
    text-transform: uppercase;
    color: var(--logo-grey);
    white-space: nowrap;
  }
  .card-front .brand { left: 36px; top: 52px; }
  .front-rule {
    position: absolute;
    left: 310px; right: 30px; top: 64px;
    height: 1px; background: var(--rule);
  }
  .holder { position: absolute; left: 0; top: 150px; }
  .holder-bar {
    position: absolute; left: 0; top: 4px;
    width: 16px; height: 36px;
    background: linear-gradient(var(--accent-black) 0 50%, var(--accent-red) 50% 100%);
  }
  .holder-name {
    position: absolute; left: 28px; top: 0;
    font-weight: 700; font-size: 21px; color: var(--ink);
    letter-spacing: 0.5px; white-space: nowrap;
  }
  .holder-role {
    position: absolute; left: 28px; top: 28px;
    font-size: 12px; color: var(--accent-red);
    letter-spacing: 1px;
  }
  .address {
    position: absolute; left: 36px; top: 214px;
    font-size: 13px; line-height: 1.5; color: var(--ink-soft);
    font-style: normal;
  }
  .contact {
    position: absolute; right: 36px; top: 150px;
    list-style: none; font-size: 12px; line-height: 1.75; color: var(--ink-soft);
  }
  .contact li { display: flex; align-items: center; gap: 6px; white-space: nowrap; }
  .contact svg { width: 11px; height: 11px; flex: none; }
  /* back */
  .card-back {
    left: 640px;
    background: linear-gradient(160deg, var(--silver-light) 0%, var(--silver-mid) 55%, var(--silver-dark) 100%);
  }
  .card-back .brand { right: 34px; top: 44px; }
  .card-back .brand-dot { background: var(--on-silver); }
  .card-back .brand-name { color: var(--on-silver); }
  .services {
    position: absolute; left: 34px; bottom: 28px;
    color: var(--on-silver);
  }
  .services-title { font-weight: 600; font-size: 14px; margin-bottom: 2px; }
  .services-list { list-style: none; font-size: 13px; line-height: 1.45; }
  .services-list li { display: flex; align-items: center; gap: 8px; }
  .services-list li::before {
    content: ""; width: 10px; height: 10px; border-radius: 50%;
    background: var(--accent-red); flex: none;
  }
</style>
</head>
<body>

<section class="card card-front" aria-label="Business card front">
  <div class="brand">
    <span class="brand-dot"></span>
    <span class="brand-name">Pennington Dowe<br>Aesthetics</span>
  </div>
  <div class="front-rule"></div>
  <div class="holder">
    <span class="holder-bar"></span>
    <span class="holder-name">MIRA HOLT</span>
    <span class="holder-role">OWNER</span>
  </div>
  <address class="address">52 Farrowmere Road<br>4 Brackwell High Street, KT9 4WQ</address>
  <ul class="contact">
    <li>
      <svg viewBox="0 0 12 12" aria-hidden="true"><path d="M2.4 1h2l1 2.6-1.3 1a6.5 6.5 0 0 0 3.3 3.3l1-1.3L11 7.6v2A1.4 1.4 0 0 1 9.6 11 8.6 8.6 0 0 1 1 2.4 1.4 1.4 0 0 1 2.4 1z" fill="#e0141e"/></svg>
      0208 794 2160
    </li>
    <li>
      <svg viewBox="0 0 12 12" aria-hidden="true"><circle cx="6" cy="6" r="5.2" fill="none" stroke="#e0141e" stroke-width="1.3"/><path d="M1 6h10M6 1c-2.2 2.6-2.2 7.4 0 10M6 1c2.2 2.6 2.2 7.4 0 10" fill="none" stroke="#e0141e" stroke-width="1"/></svg>
      www.penningtondoweaesthetics.co.uk
    </li>
  </ul>
</section>

<section class="card card-back" aria-label="Business card back">
  <div class="brand">
    <span class="brand-dot"></span>
    <span class="brand-name">Pennington Dowe<br>Aesthetics</span>
  </div>
  <div class="services">
    <p class="services-title">Specializing in:</p>
    <ul class="services-list">
      <li>Quorvex</li>
      <li>Lip Enhancement</li>
      <li>Chemical Peels</li>
      <li>Facial Fillers</li>
      <li>Non-Surgical Face Lift</li>
    </ul>
  </div>
</section>

</body>
</html>
```